business card for KestrelLine Construction
need a tag line (here to meet your needs)?
business card for KestrelLine Construction -
Creative Brief
Simple
Lorcan Whitlaney
Foreman
New Jersey or servicing north jersey
info@Kestrel-Line.com
www.Kestrel-Line.com
fully licensed fully insured
logo. residential commercial. 24hr emergency service. specializing in: *roofs *chimneys *masonry *gutters
logo. pic of workvan with logo Notes:________________________________________________________________________________________

```html
<!DOCTYPE html>
<html lang="en">
<head>
<meta charset="utf-8">
<title>KestrelLine Construction – Business Cards</title>
<link rel="stylesheet" href="https://fonts.googleapis.com/css2?family=Open+Sans:wght@400;600;700;800&display=swap">
<style>
  :root{
    --navy:#1f2f8c;
    --orange:#f6a11f;
    --white:#ffffff;
    --paper:#fbfbfb;
    --stage:#e9e9ec;
    --ink-soft:#5a5f80;
  }
  *{box-sizing:border-box;margin:0;padding:0}
  html,body{width:1200px;height:852px;overflow:hidden}
  body{background:var(--stage);font-family:"Open Sans",Arial,sans-serif;position:relative}
  .card{position:absolute;left:250px;width:700px;height:400px;border-radius:22px;overflow:hidden;background:var(--paper);box-shadow:0 2px 8px rgba(0,0,0,.18)}
  .card--blue-left{top:20px}
  .card--blue-right{top:432px}
  .card__shapes{position:absolute;inset:0;width:700px;height:400px}
  .holder{position:absolute;color:var(--white)}
  .holder__name{font-size:22px;font-weight:700;line-height:1.2}
  .holder__role{font-size:15px;font-weight:400;opacity:.9}
  .area{position:absolute;color:var(--white);font-size:15px}
  .contacts{position:absolute;list-style:none;color:var(--white);font-size:14.5px}
  .contacts li{display:flex;align-items:center;gap:10px;height:24px}
  .icon{width:18px;height:18px;flex:none}
  .specialties{position:absolute;color:var(--white)}
  .specialties__label{font-size:15px;font-weight:700}
  .specialties__list{font-size:15px;font-weight:700;margin-top:8px;letter-spacing:.2px;white-space:nowrap}
  .brand{position:absolute;color:var(--navy)}
  .brand__name{font-size:38px;font-weight:800;line-height:1;letter-spacing:-.5px}
  .brand__name span{display:block;font-size:22px;letter-spacing:1px;margin-top:2px}
  .brand__tagline{font-size:11.5px;font-weight:600;color:var(--ink-soft);margin-top:10px;white-space:nowrap}
  .align-right{text-align:right}
  .align-right.contacts li{justify-content:flex-end}
</style>
</head>
<body>

<section class="card card--blue-left">
  <svg class="card__shapes" viewBox="0 0 700 400" aria-hidden="true">
    <path d="M0 0H292C330 160 470 320 700 352V400H0Z" fill="var(--navy)"/>
    <path d="M292 0H336C372 150 500 300 700 332V352C470 320 330 160 292 0Z" fill="var(--orange)"/>
  </svg>

  <div class="holder" style="left:36px;top:44px">
    <div class="holder__name">Lorcan Whitlaney</div>
    <div class="holder__role">Foreman</div>
  </div>

  <div class="area" style="left:60px;top:138px">Servicing North Jersey</div>

  <ul class="contacts" style="left:36px;top:166px">
    <li><svg class="icon" viewBox="0 0 20 20"><path d="M5 2l3 4-2 2c1 3 3 5 6 6l2-2 4 3-2 3C8 18 2 12 2 4z" fill="var(--white)"/></svg>(T)1-888-555-0142</li>
    <li><svg class="icon" viewBox="0 0 20 20"><path d="M5 2l3 4-2 2c1 3 3 5 6 6l2-2 4 3-2 3C8 18 2 12 2 4z" fill="var(--white)"/></svg>201-555-0187</li>
    <li><svg class="icon" viewBox="0 0 20 20"><circle cx="10" cy="10" r="9" fill="var(--white)"/><text x="10" y="14.5" text-anchor="middle" font-size="13" font-weight="700" fill="var(--navy)" font-family="Open Sans, sans-serif">@</text></svg>info@Kestrel-Line.com</li>
    <li><svg class="icon" viewBox="0 0 20 20"><circle cx="10" cy="10" r="8" fill="none" stroke="var(--white)" stroke-width="2"/><path d="M2 10h16M10 2c-4 5-4 11 0 16M10 2c4 5 4 11 0 16" fill="none" stroke="var(--white)" stroke-width="1.4"/></svg>www.Kestrel-Line.com</li>
  </ul>

  <div class="specialties" style="left:36px;top:300px">
    <div class="specialties__label">Specializing in :</div>
    <div class="specialties__list">roofs / chimneys / masonry / gutters</div>
  </div>

  <div class="brand" style="left:410px;top:48px">
    <div class="brand__name">KestrelLine<span>CONSTRUCTION</span></div>
    <div class="brand__tagline">Residential &amp; Commercial.&nbsp;&nbsp;24hr emergency service.</div>
  </div>
</section>

<section class="card card--blue-right">
  <svg class="card__shapes" viewBox="0 0 700 400" aria-hidden="true">
    <path d="M700 0H470C430 170 260 330 0 362V400H700Z" fill="var(--navy)"/>
    <path d="M470 0H424C390 160 230 310 0 340V362C260 330 430 170 470 0Z" fill="var(--orange)"/>
  </svg>

  <div class="holder align-right" style="right:36px;top:44px">
    <div class="holder__name">Lorcan Whitlaney</div>
    <div class="holder__role">Foreman</div>
  </div>

  <div class="area align-right" style="right:60px;top:138px">Servicing North Jersey</div>

  <ul class="contacts align-right" style="right:36px;top:166px">
    <li>(T)1-888-555-0142<svg class="icon" viewBox="0 0 20 20"><path d="M5 2l3 4-2 2c1 3 3 5 6 6l2-2 4 3-2 3C8 18 2 12 2 4z" fill="var(--white)"/></svg></li>
    <li>201-555-0187<svg class="icon" viewBox="0 0 20 20"><path d="M5 2l3 4-2 2c1 3 3 5 6 6l2-2 4 3-2 3C8 18 2 12 2 4z" fill="var(--white)"/></svg></li>
    <li>info@Kestrel-Line.com<svg class="icon" viewBox="0 0 20 20"><circle cx="10" cy="10" r="9" fill="var(--white)"/><text x="10" y="14.5" text-anchor="middle" font-size="13" font-weight="700" fill="var(--navy)" font-family="Open Sans, sans-serif">@</text></svg></li>
    <li>www.Kestrel-Line.com<svg class="icon" viewBox="0 0 20 20"><circle cx="10" cy="10" r="8" fill="none" stroke="var(--white)" stroke-width="2"/><path d="M2 10h16M10 2c-4 5-4 11 0 16M10 2c4 5 4 11 0 16" fill="none" stroke="var(--white)" stroke-width="1.4"/></svg></li>
  </ul>

  <div class="specialties align-right" style="right:36px;top:300px">
    <div class="specialties__label">Specializing in :</div>
    <div class="specialties__list">roofs / chimneys / masonry / gutters</div>
  </div>

  <div class="brand" style="left:40px;top:70px">
    <div class="brand__name">KestrelLine<span>CONSTRUCTION</span></div>
    <div class="brand__tagline">Residential &amp; Commercial.&nbsp;&nbsp;24hr emergency service.</div>
  </div>
</section>

</body>
</html>
```